Bref créative
Stationary - Morvane Advisory
Business Card, Letterhead & Pen Design
Professional
Helmut Draven
Director
Address line 1
Address line 2
Address line 3
Address line 4
Post Code
QRP@QRP.example
For the business card I like the idea of front/back designs, where either there is something which joins the front and back or there is a slightly modified logo on the back... You're call, I'm open to anything here, so if you come up with something just try it out, I'll give everyone feedback where possible!
Please don't just stick my logo on a pen and say "hey, here you go...", for the pen design I'm looking for colours etc and where they are placed on the pen too!
Anything you think would look good!
Image file to show the logo
Extra images (inc psds!) for the logo

```html
<!DOCTYPE html>
<html lang="en">
<head>
<meta charset="utf-8">
<title>Morvane Advisory — Stationery Set</title>
<link rel="stylesheet" href="https://fonts.googleapis.com/css2?family=Montserrat:wght@500&family=Open+Sans:wght@400;600&display=swap">
<style>
  :root {
    --backdrop: #e9e6e1;
    --paper: #ffffff;
    --paper-edge: #d9dde0;
    --teal: #1a8fb0;
    --teal-deep: #0b5f7c;
    --teal-light: #4fb8d6;
    --ink: #3d4448;
    --ink-soft: #7b858b;
    --ghost: rgba(26, 143, 176, 0.08);
  }
  * { box-sizing: border-box; margin: 0; padding: 0; }
  html, body { width: 1200px; height: 674px; overflow: hidden; }
  body {
    background: var(--backdrop);
    font-family: "Open Sans", Arial, sans-serif;
    color: var(--ink);
    position: relative;
  }
  .piece {
    position: absolute;
    background: var(--paper);
    box-shadow: 0 2px 8px rgba(0,0,0,0.12);
    overflow: hidden;
    border: 1px solid var(--paper-edge);
  }
  .wordmark {
    font-family: "Montserrat", Arial, sans-serif;
    font-weight: 500;
    color: var(--teal);
    white-space: nowrap;
    letter-spacing: 0.3px;
  }
  .wordmark-square {
    display: inline-block;
    background: var(--teal);
    border-radius: 4px;
  }
  .ghost-square {
    position: absolute;
    background: var(--ghost);
    border-radius: 14px;
  }

  /* Business card front */
  .card-front { left: 132px; top: 168px; width: 264px; height: 90px; }
  .card-front .wordmark {
    position: absolute; left: 0; right: 0; top: 30px;
    text-align: center; font-size: 22px;
  }

  /* Business card back */
  .card-back { left: 100px; top: 305px; width: 268px; height: 122px; }
  .card-back .brand-panel {
    position: absolute; left: 10px; top: 26px; width: 68px; height: 68px;
    background: linear-gradient(160deg, var(--teal-light), var(--teal-deep));
    border-radius: 6px;
  }
  .card-back .details {
    position: absolute; left: 90px; top: 28px;
    font-size: 7.5px; line-height: 1.45; color: var(--ink-soft); white-space: nowrap;
  }
  .card-back .person { font-size: 11px; font-weight: 600; color: var(--teal); }
  .card-back .role { font-size: 7.5px; margin-bottom: 6px; }

  /* Letterhead */
  .letterhead { left: 434px; top: 48px; width: 423px; height: 547px; }
  .letterhead .masthead {
    position: absolute; left: 22px; top: 28px;
    display: flex; align-items: center; gap: 7px;
  }
  .letterhead .masthead .wordmark-square { width: 20px; height: 20px; }
  .letterhead .masthead .wordmark { font-size: 20px; }
  .letterhead .divider { position: absolute; left: 272px; top: 24px; width: 1px; height: 40px; background: var(--teal); }
  .letterhead .address {
    position: absolute; left: 282px; top: 26px;
    font-size: 6.5px; line-height: 1.5; color: var(--ink-soft); white-space: nowrap;
  }
  .letterhead .address .contact { margin-top: 5px; }
  .letterhead .ghost-square { left: -30px; top: 200px; width: 170px; height: 170px; }

  /* Envelope */
  .envelope { left: 679px; top: 240px; width: 389px; height: 259px; }
  .envelope .flap { position: absolute; left: 0; top: 0; width: 389px; height: 100px; }
  .envelope .wordmark { position: absolute; left: 30px; top: 76px; font-size: 26px; }
  .envelope .ghost-square { right: 14px; top: 132px; width: 92px; height: 92px; }
  .envelope .address {
    position: absolute; left: 28px; bottom: 20px;
    font-size: 6.5px; color: var(--ink-soft); white-space: nowrap;
  }
</style>
</head>
<body>

  <section class="piece card-front" aria-label="Business card front">
    <div class="wordmark">Morvane Advisory</div>
  </section>

  <section class="piece card-back" aria-label="Business card back">
    <div class="brand-panel"></div>
    <div class="details">
      <div class="person">Helmut Draven</div>
      <div class="role">Director</div>
      <div>Address line 1, Address line 2</div>
      <div>Address line 3, Address line 4, Post Code</div>
      <div>T: 0000 000 000</div>
      <div>QRP@QRP.example</div>
    </div>
  </section>

  <section class="piece letterhead" aria-label="Letterhead">
    <div class="masthead">
      <span class="wordmark-square"></span>
      <span class="wordmark">Morvane Advisory</span>
    </div>
    <div class="divider"></div>
    <div class="address">
      <div>Address line 1, Address line 2</div>
      <div>Address line 3, Post Code</div>
      <div class="contact">T: 0000 000 000</div>
      <div>QRP@QRP.example</div>
    </div>
    <div class="ghost-square"></div>
  </section>

  <section class="piece envelope" aria-label="Envelope">
    <svg class="flap" viewBox="0 0 389 100" preserveAspectRatio="none">
      <defs>
        <linearGradient id="flap-band" x1="0" y1="0" x2="1" y2="0">
          <stop offset="0" stop-color="#4fb8d6"/>
          <stop offset="1" stop-color="#0b5f7c"/>
        </linearGradient>
      </defs>
      <path d="M0 0 H389 V62 C300 18 110 26 0 56 Z" fill="url(#flap-band)"/>
    </svg>
    <div class="wordmark">Morvane Advisory</div>
    <div class="ghost-square"></div>
    <div class="address">Address line 1, Address line 2, Address line 3, Post Code</div>
  </section>

</body>
</html>
```